BrickPlayo Business Card

We need a business card design for our company. We sell construction-themed amusement rides for kids.

Contact Information for Business Card

Contact info on business card should include:
Lars Wendt
Co-Founder & COO
(833) 527-BRIKPLA
Lars@brickplayo.com
www.brickplayo.com

```html
<!DOCTYPE html>
<html lang="en">
<head>
<meta charset="utf-8">
<title>BrickPlayo Business Card</title>
<link rel="stylesheet" href="https://fonts.googleapis.com/css2?family=Bowlby+One&family=Ubuntu:wght@400;500;700&display=swap">
<style>
  :root {
    --page-bg: #1c1c1d;
    --card-bg: #0b0b0c;
    --edge-blue: #29a8e0;
    --name-red: #f04e23;
    --accent-orange: #f7941d;
    --watermark: #2a1a14;
    --art-warm: #6a3a22;
    --art-cool: #25324f;
  }
  * { margin: 0; padding: 0; box-sizing: border-box; }
  html, body { width: 1200px; height: 900px; overflow: hidden; background: var(--page-bg); }
  .canvas {
    width: 1200px; height: 900px;
    display: flex; flex-direction: column; align-items: center; justify-content: center; gap: 30px;
  }
  .card {
    position: relative; width: 700px; height: 400px;
    background: var(--card-bg);
    border-left: 4px solid var(--edge-blue);
    border-bottom: 4px solid var(--edge-blue);
    overflow: hidden;
    box-shadow: 0 14px 30px rgba(0,0,0,.55);
  }
  /* front */
  .front-watermark {
    position: absolute; left: 24px; top: 150px;
    font-family: "Ubuntu", sans-serif; font-weight: 700;
    font-size: 112px; letter-spacing: -2px; line-height: 1;
    color: var(--watermark); white-space: nowrap;
  }
  .front-art {
    position: absolute; left: 220px; top: 60px; width: 400px; height: 336px;
    border-radius: 16px;
    background: linear-gradient(180deg, var(--art-warm), var(--art-cool));
    opacity: .85;
  }
  /* back */
  .person-name {
    position: absolute; left: 140px; top: 62px;
    font-family: "Bowlby One", sans-serif; font-weight: 400; font-size: 36px; line-height: 1;
    color: var(--name-red); white-space: nowrap;
  }
  .person-title {
    position: absolute; left: 140px; top: 106px;
    font-family: "Ubuntu", sans-serif; font-size: 18px;
    color: var(--accent-orange); white-space: nowrap;
  }
  .rule { position: absolute; left: 0; height: 2px; background: var(--accent-orange); }
  .rule-top { top: 145px; width: 340px; }
  .rule-bottom { top: 270px; width: 300px; }
  .contact {
    position: absolute; display: flex; align-items: center; gap: 10px;
    font-family: "Ubuntu", sans-serif; font-size: 19px; color: var(--accent-orange);
    white-space: nowrap;
  }
  .contact svg { width: 18px; height: 18px; flex: none; }
  .contact-phone { left: 110px; top: 182px; }
  .contact-email { left: 110px; top: 212px; }
  .contact-web { left: 80px; top: 320px; }
  .contact-web strong { font-weight: 700; }
  .brand-name {
    position: absolute; left: 390px; top: 160px;
    display: flex; align-items: center; gap: 12px;
    font-family: "Ubuntu", sans-serif; font-weight: 700; font-size: 46px;
    color: var(--accent-orange); white-space: nowrap;
  }
  .brand-name .brand-square { width: 24px; height: 24px; background: var(--accent-orange); }
</style>
</head>
<body>
<main class="canvas">
  <section class="card card-front">
    <div class="front-watermark">BrickPlayo</div>
    <div class="front-art" role="img" aria-label="Illustration of two cartoon construction workers in hard hats"></div>
  </section>

  <section class="card card-back">
    <h1 class="person-name">Lars Wendt</h1>
    <p class="person-title">Co-Founder &amp; COO</p>
    <div class="rule rule-top"></div>

    <p class="contact contact-phone">
      <svg viewBox="0 0 20 20" fill="none" stroke="currentColor" stroke-width="1.6"><circle cx="10" cy="10" r="8.5"/><path d="M7 6c-.8.6-.8 2 .4 3.8s2.8 3 3.8 3.3c1 .3 1.8-.2 2-.9l-1.6-1.2-.9.7c-.8-.3-2-1.6-2.4-2.4l.7-.9L8 6.9z"/></svg>
      (833) 527-BRIKPLA
    </p>
    <p class="contact contact-email">
      <svg viewBox="0 0 20 20" fill="none" stroke="currentColor" stroke-width="1.6"><rect x="2" y="4.5" width="16" height="11"/><path d="M2 4.5l8 6 8-6"/></svg>
      Lars@brickplayo.com
    </p>
    <div class="rule rule-bottom"></div>

    <p class="contact contact-web">
      <svg viewBox="0 0 20 20" fill="none" stroke="currentColor" stroke-width="1.6"><circle cx="10" cy="10" r="8.5"/><ellipse cx="10" cy="10" rx="3.8" ry="8.5"/><path d="M1.5 10h17M3 5.5h14M3 14.5h14"/></svg>
      <span>www.<strong>brickplayo</strong>.com</span>
    </p>

    <div class="brand-name"><span>BrickPlayo</span><span class="brand-square"></span></div>
  </section>
</main>
</body>
</html>
```